Massage Center New Ad

You will be creating a 5 X 7" Massage Ad.
All the text content remains the same as example provided
however looking for a "COMPLETELY DIFFERENT" Look.
Feel free to use photo images, clip art images, Black & white, etc. Remember it should different than example.
Emphasis on the PROMO of a 30 minute massage for Only $15. Logo Attached.
Reason: Still looking for the piece that stands out....Thanks
Massage

```html
<!DOCTYPE html>
<html lang="en">
<head>
<meta charset="utf-8">
<title>Coral Cove Massage Centers – Grand Opening</title>
<link href="https://fonts.googleapis.com/css2?family=Open+Sans:wght@400;600;800&family=Archivo+Black&family=Playfair+Display:ital,wght@1,900&family=Marcellus&display=swap" rel="stylesheet">
<style>
  :root{
    --espresso:#2b1f1a;
    --cream:#f6efe4;
    --promo-red:#d9302b;
    --gold:#f5b800;
    --sand:#d8c7ad;
    --photo-light:#d6d6d6;
    --photo-dark:#3c3c3c;
    --white:#ffffff;
  }
  *{margin:0;padding:0;box-sizing:border-box;}
  html,body{width:1200px;height:857px;overflow:hidden;background:var(--cream);}
  .ad{position:relative;width:1200px;height:857px;overflow:hidden;background:var(--cream);
    font-family:"Open Sans",sans-serif;color:var(--espresso);}

  /* left column: photo with services panel */
  .hero-photo{position:absolute;left:0;top:0;width:460px;height:857px;
    background:linear-gradient(160deg,var(--photo-light) 0%,#a8a8a8 40%,#6e6e6e 70%,var(--photo-dark) 100%);}
  .column-rule{position:absolute;left:460px;top:0;width:10px;height:857px;background:var(--gold);}
  .services-panel{position:absolute;left:0;top:480px;width:460px;height:377px;
    background:rgba(43,31,26,.9);padding:34px 0 0;}
  .services-heading{width:140px;height:4px;background:var(--gold);margin:0 auto 22px;}
  .service-list{list-style:none;text-align:center;color:var(--cream);font-size:24px;line-height:42px;font-weight:600;}

  /* right column */
  .content{position:absolute;left:510px;top:0;width:650px;height:857px;}

  .headline{position:absolute;left:0;top:36px;width:650px;text-align:center;}
  .headline-grand{display:block;font-family:"Playfair Display",serif;font-style:italic;font-weight:900;
    font-size:64px;line-height:1;color:var(--promo-red);}
  .headline-opening{display:block;font-family:"Archivo Black",sans-serif;font-size:86px;line-height:1.02;
    color:var(--espresso);letter-spacing:1px;}

  .promo-card{position:absolute;left:0;top:210px;width:650px;height:250px;background:var(--promo-red);
    border-radius:14px;text-align:center;padding-top:22px;box-shadow:0 8px 0 var(--espresso);}
  .promo-title{font-family:"Archivo Black",sans-serif;font-size:44px;line-height:1.1;color:var(--white);}
  .promo-price-row{display:flex;justify-content:center;align-items:baseline;gap:22px;margin-top:2px;}
  .promo-only{font-family:"Archivo Black",sans-serif;font-size:42px;color:var(--white);}
  .promo-price{font-family:"Archivo Black",sans-serif;font-size:134px;line-height:1.1;color:var(--gold);}
  .promo-terms{position:absolute;left:0;top:478px;width:650px;text-align:center;font-size:16px;color:#4a3d36;}

  .tagline{position:absolute;left:0;top:515px;width:650px;text-align:center;font-family:"Marcellus",serif;}
  .tagline-title{font-size:56px;line-height:1.1;}
  .tagline-sub{font-size:26px;line-height:1.3;}

  .divider{position:absolute;left:175px;top:632px;width:300px;height:3px;background:var(--sand);}

  .contact{position:absolute;left:0;top:652px;width:650px;text-align:center;font-weight:800;}
  .contact-city{font-size:34px;line-height:1.25;}
  .contact-phone{font-size:42px;line-height:1.2;color:var(--promo-red);}

  .brand{position:absolute;left:0;top:780px;width:650px;display:flex;justify-content:center;align-items:center;gap:14px;
    font-weight:800;font-size:26px;color:var(--espresso);}
  .brand-dot{flex:none;width:30px;height:30px;border-radius:50%;background:var(--gold);}
</style>
</head>
<body>
<div class="ad">
  <div class="hero-photo" role="img" aria-label="Black and white photo of a therapist's hands massaging a client's back beside a white towel"></div>
  <div class="column-rule"></div>

  <div class="services-panel">
    <div class="services-heading"></div>
    <ul class="service-list">
      <li>Reflexology</li>
      <li>Sports Massage</li>
      <li>Trigger Point Therapy</li>
      <li>Relaxation Massage</li>
      <li>Deep Tissue</li>
      <li>Injury Massage</li>
      <li>Swedish</li>
    </ul>
  </div>

  <div class="content">
    <h1 class="headline">
      <span class="headline-grand">Grand</span>
      <span class="headline-opening">OPENING!</span>
    </h1>

    <div class="promo-card">
      <p class="promo-title">30 Minute Massage</p>
      <p class="promo-price-row"><span class="promo-only">only</span><span class="promo-price">$15</span></p>
    </div>
    <p class="promo-terms">(30 Minutes/$35 Value w/ad 1x only)</p>

    <div class="tagline">
      <p class="tagline-title">Massage</p>
      <p class="tagline-sub">Licensed Professional Stress Relief</p>
    </div>

    <div class="divider"></div>

    <div class="contact">
      <p class="contact-city">New Location - New City</p>
      <p class="contact-phone">000.000.0000</p>
    </div>

    <div class="brand">
      <span class="brand-dot"></span>
      <span class="brand-name">Coral Cove Massage Centers</span>
    </div>
  </div>
</div>
</body>
</html>
```